Business card/ Letterhead/ Envelope Design for Dental Office
Brent Vasko
Business card/ Letterhead/ Envelope Design for Dental Office  - Health
Creative Brief
Professional
4275 Larkspur Ln Ste 200
vaskodds@pinehollowdental.example
vaskodds vaskodds
if you can update all the ones with ratings that'd be great to see updates. 1) change name to read Brent K. Vasko D.D.S. 2) under name if you can add General Dentist 3) will need full address: 4275 Larkspur Ln Ste 200 Sun Prairie, WI 53590 4) include fax number (608) 555-0147

```html
<!DOCTYPE html>
<html lang="en">
<head>
<meta charset="utf-8">
<title>Pine Hollow Dental Center — Business Card</title>
<link rel="stylesheet" href="https://fonts.googleapis.com/css2?family=Jost:wght@400;500;600&display=swap">
<style>
  :root {
    --backdrop: #e9ebee;
    --card: #ffffff;
    --brand-blue: #1f63a8;
    --navy: #123d73;
    --sky: #3a8fd6;
    --ink: #2b3a4a;
    --muted: #5c6876;
    --icon: #4f9ad8;
  }
  * { margin: 0; padding: 0; box-sizing: border-box; }
  html, body {
    width: 1200px; height: 901px; overflow: hidden;
    background: var(--backdrop);
    font-family: "Jost", Arial, sans-serif;
  }
  .sheet {
    width: 1200px; height: 901px;
    display: flex; flex-direction: column;
    align-items: center; justify-content: center; gap: 56px;
  }
  .card {
    position: relative;
    width: 560px; height: 320px;
    background: var(--card);
    box-shadow: 0 6px 18px rgba(20, 35, 55, 0.18);
    overflow: hidden;
  }
  .brand { display: flex; align-items: center; gap: 12px; }
  .brand-dot {
    width: 30px; height: 30px; border-radius: 50%;
    background: var(--brand-blue); flex: none;
  }
  .brand-name {
    color: var(--brand-blue); font-weight: 600;
    font-size: 26px; line-height: 1.05; letter-spacing: 0.2px;
  }
  .card-front .brand {
    position: absolute; left: 50%; top: 50%;
    transform: translate(-50%, -50%);
  }
  .card-back .brand { position: absolute; left: 40px; top: 116px; }
  .card-back .brand-name { font-size: 24px; }
  .contact {
    position: absolute; left: 300px; top: 70px; width: 240px;
    color: var(--ink);
  }
  .contact-name {
    font-size: 17px; font-weight: 500; color: var(--ink);
    line-height: 1.2;
  }
  .contact-role {
    font-size: 12px; font-weight: 400; color: var(--muted);
    margin: 2px 0 12px;
  }
  .contact-list { list-style: none; }
  .contact-list li {
    display: flex; align-items: flex-start; gap: 8px;
    font-size: 12px; line-height: 1.35; color: var(--muted);
    margin-bottom: 5px;
  }
  .contact-list svg { width: 11px; height: 11px; flex: none; fill: var(--icon); margin-top: 3px; }
  .band {
    position: absolute; left: 0; bottom: 0;
    width: 560px; height: 30px; display: block;
  }
</style>
</head>
<body>
<main class="sheet">
  <section class="card card-front" aria-label="Card front">
    <div class="brand">
      <span class="brand-dot"></span>
      <span class="brand-name">Pine Hollow<br>Dental Center</span>
    </div>
  </section>

  <section class="card card-back" aria-label="Card back">
    <div class="brand">
      <span class="brand-dot"></span>
      <span class="brand-name">Pine Hollow<br>Dental Center</span>
    </div>

    <div class="contact">
      <p class="contact-name">Brent K. Vasko D.D.S.</p>
      <p class="contact-role">General Dentist</p>
      <ul class="contact-list">
        <li>
          <svg viewBox="0 0 12 12" aria-hidden="true"><path d="M6 0.5a4 4 0 0 0-4 4c0 3 4 7 4 7s4-4 4-7a4 4 0 0 0-4-4zm0 5.5a1.5 1.5 0 1 1 0-3 1.5 1.5 0 0 1 0 3z"/></svg>
          <span>4275 Larkspur Ln Ste 200<br>Sun Prairie, WI 53590</span>
        </li>
        <li>
          <svg viewBox="0 0 12 12" aria-hidden="true"><path d="M3 0.8l1.8 2.4-1 1.3c.7 1.6 2 2.9 3.6 3.6l1.3-1 2.4 1.8-1 2.1C5 10.8 1.2 7 1 2z"/></svg>
          <span>608-555-0192</span>
        </li>
        <li>
          <svg viewBox="0 0 12 12" aria-hidden="true"><path d="M3 1h5v3H3z M1 4.5h10v5H9V8H3v1.5H1z M3 8.5h6V11H3z"/></svg>
          <span>Fax (608) 555-0147</span>
        </li>
        <li>
          <svg viewBox="0 0 12 12" aria-hidden="true"><path d="M1 2.5h10v7H1z M1.5 3l4.5 3.5L10.5 3" stroke="#fff" stroke-width="0.9"/></svg>
          <span>vaskodds@pinehollowdental.example</span>
        </li>
      </ul>
    </div>

    <svg class="band" viewBox="0 0 560 30" aria-hidden="true">
      <rect x="0" y="8" width="560" height="22" fill="var(--sky)"/>
      <polygon points="0,8 250,8 236,30 0,30" fill="var(--navy)"/>
    </svg>
  </section>
</main>
</body>
</html>
```